Lift Her Forward, 2019 Save The Date

Please develop a save the date flyer our 4th Annual Lift Her Forward and See Her Rise! This event is focused on maintaining participation and appreciation for women in the design and construction industry.

This unique Forum provides a venue to engage everyone from executives to those just beginning their careers with active, hands-on sessions and vibrant networking with the best and brightest in the A/E/C industry. In our usual Q-TarVM Forum style, Keynotes become table participants and table participants become presenters, encouraging participants to assimilate what they are learning. Join local, state and national leaders and subject matter experts as we candidly explore and address the issues affecting women in our industry.

Industry/Entity Type

Construction

Font styles to use
Sans Serif

Requirements
Must have
• This is a save the date, Must have:
• Q-TarVM Logo
• Title: 4th Annual Lift Her Forward and See Her Rise!
• Date: January 25, 2019
• Location: Harbor Crest Resort and Spa, San Marcos, TX
Nice to have
• A header that can easily be pulled to add to other marketing materials and for use across other platforms (web, etc.).

```html
<!DOCTYPE html>
<html lang="en">
<head>
<meta charset="utf-8">
<title>Lift Her Forward – Save The Date 2019</title>
<link rel="stylesheet" href="https://fonts.googleapis.com/css2?family=Montserrat:wght@400;700;900&family=Oswald:wght@600&family=Open+Sans:wght@400&display=swap">
<style>
  :root {
    --stage: #1c1c1c;
    --paper: #ffffff;
    --brand-blue: #2f4ea4;
    --brand-green: #8dc63f;
    --ink: #232323;
    --ink-soft: #414141;
    --ink-muted: #555555;
    --blueprint-light: #d5ddf3;
    --blueprint-deep: #5f79cb;
  }
  * { box-sizing: border-box; margin: 0; padding: 0; }
  html, body {
    width: 1200px; height: 777px; overflow: hidden;
    background: var(--stage);
  }
  .flyer {
    position: absolute;
    left: 315.5px; top: 20px;
    width: 607px; height: 786px;
    background: var(--paper);
    transform: scale(0.9377);
    transform-origin: top left;
  }
  .flyer__frame {
    position: absolute;
    left: 35px; top: 34px; width: 537px; height: 715px;
    border: 3px solid var(--brand-green);
  }
  .flyer__frame-gap {
    position: absolute;
    left: 232px; top: 30px; width: 143px; height: 10px;
    background: var(--paper);
  }
  .blueprint-area {
    position: absolute;
    left: 38px; top: 440px; width: 531px; height: 306px;
    background: linear-gradient(to bottom,
      rgba(255,255,255,0) 0%,
      var(--blueprint-light) 45%,
      var(--blueprint-deep) 100%);
    opacity: 0.75;
  }
  .centered {
    position: absolute;
    left: 35px; width: 537px;
    text-align: center;
  }
  .brand {
    top: 58px;
    display: flex; justify-content: center; align-items: center; gap: 10px;
  }
  .brand__dot {
    width: 26px; height: 26px; border-radius: 50%;
    background: var(--brand-blue);
  }
  .brand__name {
    font-family: "Montserrat", sans-serif;
    font-weight: 700; font-size: 30px;
    color: var(--brand-blue);
    letter-spacing: 0.5px;
  }
  .headline {
    top: 138px;
    font-family: "Montserrat", sans-serif;
    font-weight: 900; font-size: 80px; line-height: 62px;
    letter-spacing: -3px;
    color: var(--brand-blue);
  }
  .event-date {
    top: 268px;
    font-family: "Oswald", sans-serif;
    font-weight: 600; font-size: 28px; line-height: 34px;
    color: var(--ink-soft);
  }
  .hatch-bar {
    position: absolute;
    left: 184px; width: 238px; height: 14px;
    background: repeating-linear-gradient(70deg,
      var(--ink-soft) 0 4px, transparent 4px 7px);
  }
  .hatch-bar--upper { top: 322px; }
  .hatch-bar--lower { top: 501px; }
  .event-title {
    top: 350px;
    font-family: "Montserrat", sans-serif;
    font-weight: 900; font-size: 38px; line-height: 41px;
    letter-spacing: -0.5px;
    color: var(--brand-blue);
  }
  .venue {
    top: 468px;
    font-family: "Open Sans", sans-serif;
    font-weight: 400; font-size: 16px; line-height: 20px;
    letter-spacing: 0.6px;
    color: var(--ink-muted);
  }
  .intro {
    position: absolute;
    left: 62px; top: 534px; width: 482px;
    font-family: "Open Sans", sans-serif;
    font-size: 10px; line-height: 13px;
    text-align: justify;
    color: var(--ink);
  }
  .intro p + p { margin-top: 14px; }
</style>
</head>
<body>
  <main class="flyer">
    <div class="blueprint-area" role="img" aria-label="Faint blue architectural drawing of a building framework"></div>
    <div class="flyer__frame"></div>
    <div class="flyer__frame-gap"></div>

    <div class="centered brand">
      <span class="brand__dot"></span>
      <span class="brand__name">Q-TarVM</span>
    </div>

    <h1 class="centered headline">SAVE<br>THE DATE</h1>
    <p class="centered event-date">JANUARY 25, 2019</p>
    <div class="hatch-bar hatch-bar--upper"></div>

    <h2 class="centered event-title">4TH ANNUAL<br>LIFT HER FORWARD AND<br>SEE HER RISE!</h2>
    <p class="centered venue">HARBOR CREST RESORT AND SPA, SAN MARCOS, TX</p>
    <div class="hatch-bar hatch-bar--lower"></div>

    <div class="intro">
      <p>This unique Forum provides a venue to engage everyone from executives to those just beginning their careers with active, hands-on sessions and vibrant networking with the best and brightest in the A/E/C industry.</p>
      <p>In our usual Q-TarVM Forum style, Keynotes become table participants and table participants become presenters, encouraging participants to assimilate what they are learning.</p>
      <p>Join local, state and national leaders and subject matter experts as we candidly explore and address the issues affecting women in our industry.</p>
    </div>
  </main>
</body>
</html>
```